Brochure Design Project (Design Studio)

Items required:
1-Brochure. We suggest 15Cm X 15 Cm after cutting.
2-Business Card.
3-Head letter.
4-Folder ( folder should carry the Brochure in pocket and the business card in a pocket on the opposite side of the folder.
5-Envelope to carry everything.
This brochure is expected to draw attention of high level management in companies to the quality and creativity of the design work and encourage them to do business with us. note that brochure will be printed in high quality printing and paper.
The game plan is as follows:
Over all description, the theme of the brochure is drawn from the website theme (website will be uploaded shortly, pictures of the website are attached, logo appears in the top left corner). Please avoid direct copying from the website unless it is a creative copying, just draw the theme from there. however, we need it to be elegant, stylish and class in colors and style. This is a MUST.
Furthermore, the main items of the Brochure:
1-The Studio is not just a studio: we will take about how Branding. A file is attached of the content. (slight changes/modification can apply during the designing process)
2-The Process: this one has to be a visual illustration of the process, it has to be very creative, could be elegant arrows and comics, could be elegant drawing, could be an elegant icons. The drawing should be separate from the steps, we need to the drawing and we need to have the steps listed and commentary, or if want to integrate both in one in an artistic way. Just don’t lose track of the theme and elegance. (steps and commentary are attached, slight changes/modification can apply at anytime.
3-Our Team: another drawing of your suggestion to illustrate the team members, we need to include the names and designation as well leave a place for some of them to say what they need to say about their style of designing. I leave it for your imagination to put this all together in a nice attractive visual illustration.
4-Works: this section will generally show the works of our designers. It needs to be focused on the works themselves, client should be able to view the details of the works ( note that when it comes to brochures and websites, we don’t need to reach to the extent with which the client can read the text in those pictures of the website or brochure, but still can see the overall design clearly). Each design is to carry the name of the designer. Last thing, this section will classify works into categories, like, Brochures, Corporate identity, print design. We didn’t finalize those categories, we will provide them to you shortly, last thing to be said, we are planning to include around 25-30 designs of each sub-category, eg. Corporate identity will have 30 business card s designs and 30 stationary designs.
5-Contacts: the company contacts.
We the brochure after printing should be 15x15 Cm.
Creativity and art work is a major player in selection.
general managers, owners
Printing

```html
<!DOCTYPE html>
<html lang="en">
<head>
<meta charset="utf-8">
<title>Corvanta Studio — Brochure Cover</title>
<link rel="stylesheet" href="https://fonts.googleapis.com/css2?family=Roboto+Condensed:wght@300&family=Roboto:wght@300;700&display=swap">
<style>
  :root {
    --bg: #060606;
    --brand-red: #d0201f;
    --text-grey: #9a9c9c;
    --headline-grey: #c6c9c9;
    --muted-grey: #6e7070;
    --dot: #5a5a5a;
  }
  * { margin: 0; padding: 0; box-sizing: border-box; }
  html, body { width: 1200px; height: 1198px; overflow: hidden; background: var(--bg); }
  .cover { position: relative; width: 1200px; height: 1198px; background: var(--bg); }

  .brand { position: absolute; top: 164px; left: 0; width: 1200px; text-align: center; }
  .brand-name { font-family: "Roboto", sans-serif; font-weight: 300; font-size: 46px; line-height: 56px; color: var(--brand-red); letter-spacing: 1px; }

  .headline { position: absolute; top: 516px; left: 0; width: 1200px; text-align: center; font-family: "Roboto", sans-serif; }
  .headline-lead { font-weight: 300; font-size: 52px; line-height: 60px; color: var(--text-grey); }
  .headline-main { font-weight: 700; font-size: 68px; line-height: 68px; color: var(--headline-grey); letter-spacing: 0.5px; }

  .intro { position: absolute; top: 670px; left: 0; width: 1200px; text-align: center; font-family: "Roboto", sans-serif; font-weight: 300; font-size: 21px; line-height: 27px; color: var(--muted-grey); }

  .rule { position: absolute; left: 0; width: 1200px; border-top: 2px dotted var(--dot); }
  .rule-top { top: 871px; }
  .rule-bottom { top: 1015px; }

  .works-strip { position: absolute; top: 884px; left: 0; width: 1200px; height: 120px; display: flex; }
  .work { height: 100%; }

  .services { position: absolute; top: 1045px; left: 0; width: 1200px; text-align: center; font-family: "Roboto Condensed", sans-serif; font-weight: 300; font-size: 28px; color: var(--text-grey); }
  .contact { position: absolute; top: 1136px; left: 0; width: 1200px; text-align: center; font-family: "Roboto Condensed", sans-serif; font-weight: 300; font-size: 19px; color: var(--text-grey); }
  .sep { margin: 0 10px; }
</style>
</head>
<body>
<main class="cover">
  <header class="brand">
    <span class="brand-name">Corvanta Studio</span>
  </header>

  <h1 class="headline">
    <span class="headline-lead">Perosnify your</span><br>
    <span class="headline-main">BUSINESS</span>
  </h1>

  <p class="intro">We are more than just a creative studio;<br>we can personify your business and dress to impress!</p>

  <div class="rule rule-top"></div>
  <section class="works-strip">
    <div class="work" style="width:190px;background:linear-gradient(90deg,#ecd9dc,#e4e1e2 70%,#8a8a8a);" role="img" aria-label="Photo of an open greeting card in pink and white"></div>
    <div class="work" style="width:164px;background:linear-gradient(90deg,#e8e6e2,#6b655d 50%,#1c1c1c);" role="img" aria-label="Photo of an open printed book with black cover"></div>
    <div class="work" style="width:160px;background:linear-gradient(120deg,#f2f2f2,#2a2a2a 40%,#3b3b3b 70%,#e6e6e6);" role="img" aria-label="Photo of black folder with red seal"></div>
    <div class="work" style="width:162px;background:linear-gradient(180deg,#e9efe2,#b42630 45%,#40463f 75%,#cfe39a);" role="img" aria-label="Screenshot of a website homepage design"></div>
    <div class="work" style="width:192px;background:linear-gradient(135deg,#eeeadf,#d7b98d 50%,#f1efea);" role="img" aria-label="Photo of printed stationery and brochure spreads"></div>
    <div class="work" style="width:172px;background:linear-gradient(90deg,#f1f1f1,#9a7b72 50%,#e9e9e9);" role="img" aria-label="Photo of a folded accordion print piece"></div>
    <div class="work" style="width:160px;background:linear-gradient(135deg,#eef0f3,#1e1e1e 45%,#262626 70%,#d6d9de);" role="img" aria-label="Photo of a black product box"></div>
  </section>
  <div class="rule rule-bottom"></div>

  <p class="services">Graphic Design<span class="sep">I</span>Corporate Identity<span class="sep">I</span>Print Design<span class="sep">I</span>Web Design</p>

  <p class="contact">Tel 00 971 2 400 1290<span class="sep">I</span>Fax 00 971 2 400 1291<span class="sep">I</span>P.O. Box 70214, Harbor City<span class="sep">I</span>Web: www.corvantastudio.com</p>
</main>
</body>
</html>
```